Announcement Card

This will be an announcement card mailed to clients as a postcard. The text should be oriented book fashion (not landscape).

Text is:

DEREK T. HOLLOWAN

is pleased to announce
he is joining

BRIARCREST LAW GROUP

as a founding partner

[PHONE, ADDRESS, EMAIL]

Industry/Entity Type

Fashion

```html
<!DOCTYPE html>
<html lang="en">
<head>
<meta charset="utf-8">
<title>Announcement Postcard – Briarcrest Law Group</title>
<link rel="stylesheet" href="https://fonts.googleapis.com/css2?family=Raleway:wght@200;300;400&display=swap">
<style>
  :root {
    --page-bg: #ececea;
    --sky-teal: #4ba6c0;
    --sky-mid: #7fb8c2;
    --glow-cream: #ece7c9;
    --haze-blue: #5e86b6;
    --deep-navy: #2c4a92;
    --text-light: #ffffff;
    --text-soft: rgba(255, 255, 255, 0.82);
    --text-dark: #3e4147;
    --band-fill: rgba(250, 250, 246, 0.78);
    --address-panel: #e2e6ec;
    --address-name: #1d1d1f;
    --address-line: #6a6e78;
  }

  * { margin: 0; padding: 0; box-sizing: border-box; }

  html, body {
    width: 1200px;
    height: 512px;
    overflow: hidden;
    background: var(--page-bg);
  }

  .canvas {
    position: relative;
    width: 1200px;
    height: 512px;
    font-family: "Raleway", sans-serif;
  }

  .card {
    position: absolute;
    top: 40px;
    width: 553px;
    height: 429px;
    overflow: hidden;
    box-shadow: 0 2px 6px rgba(0, 0, 0, 0.18);
  }

  .card-front { left: 36px; }
  .card-back { left: 617px; }

  .blur-backdrop {
    position: absolute;
    inset: 0;
    background:
      radial-gradient(ellipse 45% 30% at 45% 52%, rgba(246, 240, 212, 0.95) 0%, rgba(236, 231, 201, 0.55) 45%, rgba(236, 231, 201, 0) 100%),
      radial-gradient(ellipse 80% 45% at 50% 30%, rgba(158, 205, 200, 0.6) 0%, rgba(158, 205, 200, 0) 100%),
      linear-gradient(180deg, var(--sky-teal) 0%, var(--sky-mid) 32%, #b9cdbf 50%, var(--haze-blue) 72%, var(--deep-navy) 100%);
  }

  .front-name {
    position: absolute;
    top: 72px;
    left: 0;
    width: 100%;
    text-align: center;
    color: var(--text-light);
    font-weight: 300;
    font-size: 37px;
    letter-spacing: 1px;
  }

  .front-intro {
    position: absolute;
    top: 126px;
    left: 0;
    width: 100%;
    text-align: center;
    color: var(--text-soft);
    font-weight: 300;
    font-size: 21px;
    letter-spacing: 0.5px;
  }

  .firm-band {
    position: absolute;
    top: 189px;
    left: 0;
    width: 100%;
    height: 78px;
    background: var(--band-fill);
    display: flex;
    align-items: center;
    justify-content: center;
  }

  .firm-name {
    color: var(--text-dark);
    font-weight: 200;
    font-size: 37px;
    letter-spacing: 1px;
  }

  .front-role {
    position: absolute;
    top: 282px;
    left: 0;
    width: 100%;
    text-align: center;
    color: var(--text-soft);
    font-weight: 200;
    font-size: 34px;
    letter-spacing: 1px;
  }

  .front-contact {
    position: absolute;
    top: 383px;
    left: 0;
    width: 100%;
    text-align: center;
    color: var(--text-soft);
    font-weight: 300;
    font-size: 16px;
  }

  .address-panel {
    position: absolute;
    top: 0;
    right: 0;
    width: 224px;
    height: 100%;
    background: linear-gradient(180deg, #e6ecf0 0%, #e8e9ec 60%, #d9dbe4 100%);
  }

  .address-block {
    position: absolute;
    left: 5px;
    top: 232px;
    font-size: 21px;
    line-height: 32px;
    font-weight: 400;
  }

  .recipient-name { color: var(--address-name); }
  .address-line { color: var(--address-line); }
</style>
</head>
<body>
  <main class="canvas">
    <section class="card card-front">
      <div class="blur-backdrop" role="img" aria-label="Soft blurred teal, cream and navy backdrop"></div>
      <h1 class="front-name">DEREK T. HOLLOWAN</h1>
      <p class="front-intro">is pleased to announce he is joining</p>
      <div class="firm-band">
        <h2 class="firm-name">BRIARCREST LAW GROUP</h2>
      </div>
      <p class="front-role">as a founding partner</p>
      <p class="front-contact">[phone-address-email]</p>
    </section>

    <section class="card card-back">
      <div class="blur-backdrop" role="img" aria-label="Soft blurred teal, cream and navy backdrop"></div>
      <div class="address-panel">
        <address class="address-block" style="font-style: normal;">
          <div class="recipient-name">Recipient Name</div>
          <div class="address-line">Address Line 1</div>
          <div class="address-line">Address Line 2</div>
          <div class="address-line">Address Line 3</div>
          <div class="address-line">Address Line 4</div>
        </address>
      </div>
    </section>
  </main>
</body>
</html>
```